Business Card 85x40mm - Freelance audio mixing / live event operator

I am a freelance audio operator working in live events. Mostly corporate events mixing sound for a range of entertainment, awards nights and functions. I need a new card to give to perspective clients.

The final design will convey bold professionalism with a general dark vibe. Looking for dark-ish background with some smatterings of colour added.

I have attatched my old BC for an idea of what I have liked in the past. Id like a more modern updated design (that circular design on the back is not my logo it is just a picture I found that resembled sound} . For an added element possibly a mixture of some playful colours in a way that resembles an audio wave form or sound.

I have attached a photo called "audio software" with some colourful squiggly lines; maybe incorporate elements of that into into design
Updates

Added extra $ to project Damn Pixel hives fees are unreasonable

Target Market(s)

Mostly corporate clients

Industry/Entity Type

Events

Contact Information for Business Card

Corwin Pellath
Sound | FOH | Monitors | Systems | Corporate

Digital Audio Mixing Specialist, Live Event Technical Professional,

corwinpellath@mailvexo.net, +61 402 918 357

Colors
ec1f27
ffc214
9bcb3c
6b449b

Requirements
Must have
• Dark theme
• 85x40mm dimensions
Nice to have
• some sort of imagery or design to reflect audio/sound

```html
<!DOCTYPE html>
<html lang="en">
<head>
<meta charset="utf-8">
<title>Corwin Pellath – Business Card</title>
<link rel="stylesheet" href="https://fonts.googleapis.com/css2?family=Orbitron:wght@900&family=Red+Hat+Display:wght@400;500&display=swap">
<style>
  :root {
    --page: #ffffff;
    --frame: #c8c8c8;
    --card: #000000;
    --ink: #ffffff;
    --red: #ec1f27;
    --ring: #6a0b0e;
    --yellow: #ffc214;
    --green: #9bcb3c;
    --purple: #6b449b;
  }
  * { box-sizing: border-box; margin: 0; padding: 0; }
  html, body { width: 1200px; height: 1200px; overflow: hidden; background: var(--page); }
  .canvas {
    position: relative; width: 1200px; height: 1200px;
    border: 1px solid var(--frame); background: var(--page);
    font-family: "Red Hat Display", "Helvetica Neue", Arial, sans-serif;
  }
  .card {
    position: absolute; left: 98px; width: 1004px; height: 471px;
    background: var(--card); overflow: hidden; color: var(--ink);
  }
  .card--front { top: 88px; }
  .card--back { top: 640px; }
  .card__art { position: absolute; inset: 0; }

  .waveform {
    position: absolute; left: 0; right: 0; top: 200px; height: 240px;
    background:
      radial-gradient(ellipse 50% 48% at 50% 50%, rgba(0,0,0,0) 0%, rgba(0,0,0,0) 60%, #000 100%),
      linear-gradient(90deg, var(--red) 0%, #ff4a1c 28%, var(--yellow) 40%, #d8d02a 52%, var(--green) 62%, #c03050 75%, var(--purple) 90%, #8a3fa0 100%);
    -webkit-mask: linear-gradient(180deg, transparent 0%, #000 35%, #000 65%, transparent 100%);
            mask: linear-gradient(180deg, transparent 0%, #000 35%, #000 65%, transparent 100%);
    opacity: .85;
  }

  .tagline {
    position: absolute; left: 0; right: 0; top: 407px;
    text-align: center; font-size: 27px; font-weight: 400; letter-spacing: .1px;
  }
  .sep { color: var(--red); padding: 0 8px; }

  .identity { position: absolute; left: 0; right: 0; top: 130px; text-align: center; }
  .identity__name {
    font-family: "Orbitron", "Arial Black", sans-serif; font-weight: 900;
    font-size: 40px; letter-spacing: 3px; line-height: 1; text-transform: uppercase;
  }
  .identity__services { margin-top: 14px; font-size: 28px; font-weight: 400; }
  .identity__services .sep { padding: 0 5px; }

  .contact { position: absolute; left: 0; right: 0; top: 262px; text-align: center; font-size: 32px; font-weight: 500; letter-spacing: .5px; }
  .contact__line { display: flex; justify-content: center; align-items: center; gap: 12px; height: 42px; }
  .contact__icon { fill: var(--red); }
</style>
</head>
<body>
<main class="canvas">

  <section class="card card--front">
    <svg class="card__art" width="1004" height="471" viewBox="0 0 1004 471" aria-hidden="true">
      <circle cx="502" cy="250" r="212" fill="none" stroke="var(--ring)" stroke-width="30" opacity=".7"/>
    </svg>
    <div class="waveform" role="img" aria-label="Glowing multicolour audio waveform running across the card"></div>
    <p class="tagline">Digital Audio Mixing Specialist<span class="sep">|</span>Live Event Technical Professional</p>
  </section>

  <section class="card card--back">
    <svg class="card__art" width="1004" height="471" viewBox="0 0 1004 471" aria-hidden="true">
      <defs>
        <radialGradient id="ringGlow" cx="50%" cy="50%" r="50%">
          <stop offset="82%" stop-color="#e01a22" stop-opacity="0"/>
          <stop offset="90%" stop-color="#e01a22" stop-opacity=".55"/>
          <stop offset="100%" stop-color="#e01a22" stop-opacity="0"/>
        </radialGradient>
      </defs>
      <circle cx="502" cy="236" r="345" fill="url(#ringGlow)"/>
      <circle cx="502" cy="236" r="310" fill="none" stroke="var(--ring)" stroke-width="42" opacity=".8"/>
    </svg>

    <div class="identity">
      <h1 class="identity__name">Corwin Pellath</h1>
      <p class="identity__services">Sound<span class="sep">|</span>FOH<span class="sep">|</span>Monitors<span class="sep">|</span>Systems<span class="sep">|</span>Corporate</p>
    </div>

    <div class="contact">
      <p class="contact__line">
        <svg class="contact__icon" width="18" height="30" viewBox="0 0 18 30" aria-hidden="true">
          <path d="M3 0h12a3 3 0 0 1 3 3v24a3 3 0 0 1-3 3H3a3 3 0 0 1-3-3V3a3 3 0 0 1 3-3zm0 4v19h12V4zm6 21a1.6 1.6 0 1 0 0 3.2A1.6 1.6 0 0 0 9 25z"/>
        </svg>
        <span>+61 402 918 357</span>
      </p>
      <p class="contact__line">
        <svg class="contact__icon" width="32" height="22" viewBox="0 0 32 22" aria-hidden="true">
          <path d="M0 0h32v22H0zM2 2v1l14 10L30 3V2zm0 4v14h28V6L16 16z"/>
        </svg>
        <span>corwinpellath@mailvexo.net</span>
      </p>
    </div>
  </section>

</main>
</body>
</html>
```